Hair Salon Brochure

We need a brochure for our hair salon located in Middle Tennessee called Delphine Locks of Harbor Bend. Along with standard services, we offer specialized services and accommodations for individuals on the Autism Spectrum, regardless of background or hair type.
At Delphine Locks of Harbor Bend, our mission is to create a warm and inclusive haven for individuals of all backgrounds, including those on the autism spectrum and their families. We are dedicated to providing not only exceptional hairstyling services but also hands-on education and specialized cutting techniques for clients with natural textured hair. Our goal is to empower our clients with the knowledge and tools necessary to maintain a successful hair care routine, ensuring they leave our salon feeling confident.
We believe in fostering a sense of community, where parents of younger clients are encouraged to learn the proper hair care techniques for their children, promoting healthy practices at home. Our commitment extends beyond just hair; we are here to help you embrace your true self and recognize the beauty that resides within.
At Delphine Locks of Harbor Bend, our passion is to deliver the ultimate client experience, where you can be unapologetically yourself and feel completely at ease. From the moment you step through our doors, you are welcomed not only to discuss your hair concerns but also to engage in meaningful conversations about life. Together, we will collaborate on a personalized plan to achieve your hair goals and transform the way you perceive yourself.
Always remember, when you look good, you feel good, and when you feel good, you can achieve great things. We firmly believe that every individual is 'Beautiful Beyond the Spectrum,' and we are here to celebrate that beauty with you."
https://www.delphinelocks.net/
Tagline - "Beautiful Beyond the Spectrum"

```html
<!DOCTYPE html>
<html lang="en">
<head>
<meta charset="utf-8">
<title>Delphine Locks of Harbor Bend — Trifold Brochure</title>
<link href="https://fonts.googleapis.com/css2?family=Montserrat:wght@500;700;800;900&family=Open+Sans:wght@400;600;700&family=Great+Vibes&display=swap" rel="stylesheet">
<style>
  :root{
    --blue:#1f72bd;
    --blue-deep:#0f4c8c;
    --navy:#0b2f5c;
    --orange:#f39220;
    --white:#ffffff;
    --ink:#2b2f36;
    --stage:#e9ebee;
    --photo-hair:#5a3a2a;
    --photo-skin:#c49377;
    --photo-salon:#8a8e94;
  }
  *{box-sizing:border-box;margin:0;padding:0}
  html,body{width:1200px;height:2700px;overflow:hidden;background:var(--stage)}
  body{position:relative;font-family:"Open Sans",Arial,sans-serif;color:var(--ink)}
  .spread{position:absolute;left:40px;width:1120px;height:866px;display:grid;grid-template-columns:repeat(3,1fr);background:var(--white);box-shadow:0 6px 24px rgba(0,0,0,.18);overflow:hidden}
  .spread--outside{top:380px}
  .spread--inside{top:1454px}
  .panel{position:relative;height:100%;overflow:hidden}
  .heading{font-family:"Montserrat",Arial,sans-serif;font-weight:900;font-size:25px;letter-spacing:.5px;line-height:1.1;color:var(--blue-deep)}
  .heading span{color:var(--orange)}
  .copy{font-size:12.2px;line-height:1.55;color:var(--ink)}
  .photo{position:absolute;display:block}
  .pill{display:inline-block;background:var(--orange);color:var(--white);font-family:"Montserrat",Arial,sans-serif;font-weight:800;font-size:20px;padding:8px 26px;border-radius:30px;letter-spacing:.5px}

  /* outside: owner panel */
  .owner{padding:34px 30px 0 30px}
  .owner .copy{margin-top:10px}
  .owner-portrait{position:relative;width:150px;height:150px;margin:18px 0 16px 0;border-radius:50%;border:6px solid var(--orange);background:radial-gradient(circle at 50% 40%,var(--photo-skin) 0 30%,var(--photo-hair) 55%,#2c1c14 100%)}
  .owner .photo--salon{left:0;bottom:0;width:100%;height:170px;background:linear-gradient(135deg,#9aa0a6,#6e737a 60%,#4c5157)}

  /* outside: goal panel */
  .goal{background:var(--blue);color:var(--white);padding:34px 30px 0 30px;text-align:center}
  .goal .copy{color:var(--white);margin-top:16px;text-align:center}
  .testimonial{display:flex;gap:12px;margin-top:20px;background:var(--white);border-radius:10px;padding:12px;text-align:left}
  .testimonial .photo{position:relative;flex:0 0 90px;height:120px;border-radius:8px;background:linear-gradient(160deg,#7a5a48,#3b2a22)}
  .testimonial .copy{color:var(--ink);margin:0;text-align:left;font-size:11.5px;font-style:italic}
  .located{margin-top:18px;font-size:13px;font-weight:700;line-height:1.45}
  .goal .pill{margin-top:14px}
  .contact{margin-top:14px;font-size:13px;line-height:1.55}
  .contact-line{display:flex;align-items:center;justify-content:center;gap:8px;font-weight:700;font-size:16px}
  .contact-line svg{width:26px;height:26px}
  .contact .web{color:var(--orange);font-weight:700;margin-top:6px}

  /* outside: cover */
  .cover{background:var(--white)}
  .brand{position:absolute;top:34px;left:0;width:100%;text-align:center;font-family:"Montserrat",Arial,sans-serif;font-weight:800;font-size:20px;color:var(--navy);line-height:1.25}
  .brand-mark{display:block;margin:0 auto 8px;width:22px;height:22px;border-radius:50%;background:var(--orange)}
  .cover .photo--model{left:0;top:130px;width:100%;height:440px;background:linear-gradient(180deg,#d7d8da 0%,#b69079 35%,var(--photo-hair) 70%,#3a2418 100%)}
  .cover-band{position:absolute;left:0;bottom:0;width:100%;height:330px}
  .cover-text{position:absolute;left:0;bottom:42px;width:100%;padding:0 30px;text-align:center;color:var(--white)}
  .cover-title{font-family:"Montserrat",Arial,sans-serif;font-weight:900;font-size:40px;line-height:1.05}
  .cover-script{font-family:"Great Vibes",cursive;font-size:50px;color:var(--orange);line-height:1}
  .cover-sub{font-size:13px;line-height:1.5;margin-top:10px}
  .cover-web{font-weight:700;font-size:14px;margin-top:12px}

  /* inside: belief panel */
  .belief{padding:34px 30px 0 30px}
  .belief .copy{margin-top:10px}
  .belief .heading + .copy{margin-bottom:22px}
  .belief .photo--model{left:0;bottom:0;width:100%;height:300px;background:linear-gradient(160deg,#f2efe9 0%,#c9a58d 40%,var(--photo-hair) 75%,#2e1d14 100%)}

  /* inside: services */
  .services{background:var(--blue);padding:34px 26px 0 26px}
  .services .heading{color:var(--white)}
  .services .heading span{color:var(--orange)}
  .service-list{list-style:none;margin-top:16px}
  .service-list li{display:flex;align-items:stretch;height:26px;margin-bottom:5px;background:var(--white);font-family:"Montserrat",Arial,sans-serif;font-weight:700;font-size:12px;color:var(--navy)}
  .service-list .name{flex:1;display:flex;align-items:center;padding-left:10px;white-space:nowrap;overflow:hidden}
  .service-list .price{flex:0 0 58px;display:flex;align-items:center;justify-content:center;background:var(--orange);color:var(--white)}
  .services .photo--wash{left:0;bottom:0;width:100%;height:150px;background:linear-gradient(135deg,#c8b5a6,#6e4c3a 60%,#3d2a20)}
  .services-more{background:var(--blue-deep);padding-top:34px}
  .services-more .service-list{margin-top:0}
  .services-note{margin-top:10px;font-size:11.5px;line-height:1.5;color:var(--white);font-weight:600}
  .services-more .photo--wash{height:220px;background:linear-gradient(135deg,#d9d2cb,#8a6a57 50%,#3d2a20)}
</style>
</head>
<body>

<section class="spread spread--outside">
  <article class="panel owner">
    <h2 class="heading">MEET <span>THE OWNER</span></h2>
    <p class="copy">Delphine Marsh, founder of Delphine Locks of Harbor Bend, has spent over fifteen years caring for curly, coily and textured hair. A licensed stylist and devoted parent, she built a calm, sensory-friendly salon where every client, including those on the autism spectrum, feels heard, safe and celebrated.</p>
    <div class="owner-portrait" role="img" aria-label="Portrait of the salon owner"></div>
    <h2 class="heading">OUR <span>MISSION</span></h2>
    <p class="copy">At Delphine Locks of Harbor Bend, our mission is to create a warm and inclusive haven for individuals of all backgrounds, including those on the autism spectrum and their families, with hands-on education and specialized cutting for natural textured hair.</p>
    <div class="photo photo--salon" role="img" aria-label="Photo of the salon interior with styling chairs"></div>
  </article>

  <article class="panel goal">
    <span class="pill">OUR GOAL</span>
    <p class="copy">Our goal is to empower our clients with the knowledge and tools necessary to maintain a successful hair care routine, ensuring they leave our salon feeling confident.</p>
    <div class="testimonial">
      <div class="photo" role="img" aria-label="Photo of a happy client"></div>
      <p class="copy">“I was looking for someone with experience cutting curly hair and came across Delphine. I am so glad I did! She was patient with my son, explained every step, and gave us great tips. We will definitely be back.”</p>
    </div>
    <p class="located">Located in Middle Tennessee called Delphine Locks of Harbor Bend</p>
    <span class="pill">CONTACT US</span>
    <div class="contact">
      <div class="contact-line">
        <svg viewBox="0 0 24 24" aria-hidden="true"><circle cx="12" cy="12" r="12" fill="#f39220"/><path d="M8.6 6.5l1.8 2.6-1.1 1.3a8 8 0 004.3 4.3l1.3-1.1 2.6 1.8-.9 2a2 2 0 01-2 .9A10 10 0 016.6 9a2 2 0 01.9-2z" fill="#fff"/></svg>
        (555) 240-0140
      </div>
      <p>Delphine Locks of Harbor Bend<br>418 Willow Crest Rd, Suite 12<br>Harbor Bend, TN 37000</p>
      <p class="web">www.delphinelocks.net</p>
    </div>
  </article>

  <article class="panel cover">
    <div class="brand"><span class="brand-mark"></span>Delphine Locks<br>of Harbor Bend</div>
    <div class="photo photo--model" role="img" aria-label="Photo of a woman with long glossy brown hair"></div>
    <svg class="cover-band" viewBox="0 0 373 330" preserveAspectRatio="none" aria-hidden="true">
      <path d="M0 40 C120 0 250 10 373 60 L373 330 L0 330 Z" fill="#f39220"/>
      <path d="M0 60 C120 20 250 30 373 80 L373 330 L0 330 Z" fill="#1f72bd"/>
    </svg>
    <div class="cover-text">
      <h1 class="cover-title">BEAUTIFUL<br>BEYOND</h1>
      <p class="cover-script">the Spectrum</p>
      <p class="cover-sub">Beautiful Beyond the Spectrum, and we are here to celebrate that beauty with you.</p>
      <p class="cover-web">www.delphinelocks.net</p>
    </div>
  </article>
</section>

<section class="spread spread--inside">
  <article class="panel belief">
    <h2 class="heading">WE <span>BELIEVE</span></h2>
    <p class="copy">In fostering a sense of community, where parents of younger clients are encouraged to learn the proper hair care techniques for their children, promoting healthy practices at home. Our commitment extends beyond just hair; we are here to help you embrace your true self and recognize the beauty that resides within.</p>
    <h2 class="heading">OUR <span>PASSION</span></h2>
    <p class="copy">At Delphine Locks of Harbor Bend, our passion is to deliver the ultimate client experience, where you can be unapologetically yourself and feel completely at ease. Together, we will collaborate on a personalized plan to achieve your hair goals.</p>
    <div class="photo photo--model" role="img" aria-label="Photo of a smiling woman with flowers"></div>
  </article>

  <article class="panel services">
    <h2 class="heading">OUR <span>SERVICES</span></h2>
    <ul class="service-list">
      <li><span class="name">Haircut &amp; Style</span><span class="price">$55+</span></li>
      <li><span class="name">Curl Sculpt Cut</span><span class="price">$85+</span></li>
      <li><span class="name">Up or Chin</span><span class="price">$40+</span></li>
      <li><span class="name">Conditioning Treatment</span><span class="price">$35+</span></li>
      <li><span class="name">Consultation</span><span class="price">Free</span></li>
      <li><span class="name">Express Cut</span><span class="price">$30+</span></li>
      <li><span class="name">Textured Transformation</span><span class="price">$95+</span></li>
      <li><span class="name">Relaxer</span><span class="price">$75+</span></li>
      <li><span class="name">Special Occasion Styling</span><span class="price">$80+</span></li>
      <li><span class="name">Braids</span><span class="price">$90+</span></li>
      <li><span class="name">Starter Locs w/ 2 Strand</span><span class="price">$120+</span></li>
      <li><span class="name">Loc Retwist</span><span class="price">$70+</span></li>
    </ul>
    <div class="photo photo--wash" role="img" aria-label="Photo of a client at the wash basin"></div>
  </article>

  <article class="panel services services-more">
    <ul class="service-list">
      <li><span class="name">Crochets</span><span class="price">$85+</span></li>
      <li><span class="name">Hair Detangling</span><span class="price">$40+</span></li>
      <li><span class="name">2 Strand Twist</span><span class="price">$65+</span></li>
      <li><span class="name">Silk Press</span><span class="price">$70+</span></li>
      <li><span class="name">Silk Press &amp; Trim</span><span class="price">$85+</span></li>
      <li><span class="name">Keratin Treatment</span><span class="price">$150+</span></li>
      <li><span class="name">Curl Sculpt without Education</span><span class="price">$75+</span></li>
      <li><span class="name">Loose Hair Grooming</span><span class="price">$45+</span></li>
      <li><span class="name">Service Accommodation</span><span class="price">Free</span></li>
      <li><span class="name">Starter Locs</span><span class="price">$110+</span></li>
      <li><span class="name">Loc Detox</span><span class="price">$60+</span></li>
      <li><span class="name">Shampoo &amp; Blow Dry</span><span class="price">$45+</span></li>
    </ul>
    <p class="services-note">Along with standard services, we offer specialized services and accommodations for individuals on the Autism Spectrum, regardless of background or hair type.</p>
    <div class="photo photo--wash" role="img" aria-label="Photo of a stylist washing a client's long hair"></div>
  </article>
</section>

</body>
</html>
```